Harbor Self Storage

looking for a clean sharp easy to read advertising billboard to rent units

online rentals
online payment
online check out

climate control units available
competitive rates

https://www.harbor-selfstorage-example.com/

```html
<!DOCTYPE html>
<html lang="en">
<head>
<meta charset="utf-8">
<title>Harbor Self Storage – Billboard</title>
<link rel="stylesheet" href="https://fonts.googleapis.com/css2?family=Anton&family=Archivo+Black&family=Oswald:wght@600;700&display=swap">
<style>
  :root {
    --navy: #1a1f6b;
    --red: #e8272c;
    --white: #ffffff;
    --backdrop: #e9edf2;
    --edge: #2a2a2a;
  }
  * { margin: 0; padding: 0; box-sizing: border-box; }
  html, body { width: 1200px; height: 850px; overflow: hidden; background: var(--backdrop); }
  .canvas { position: relative; width: 1200px; height: 850px; }

  .billboard {
    position: absolute; left: 40px; top: 145px;
    width: 1120px; height: 560px;
    background: var(--white);
    border: 2px solid var(--edge);
    overflow: hidden;
  }

  .brand {
    position: absolute; left: 70px; top: 48px;
    display: flex; align-items: center; gap: 34px;
  }
  .brand-dot {
    width: 130px; height: 130px; border-radius: 50%;
    background: var(--navy); flex: none;
  }
  .brand-name {
    font-family: "Oswald", sans-serif; font-weight: 700;
    color: var(--navy); text-transform: uppercase;
    line-height: 0.95;
  }
  .brand-name .line-1 { display: block; font-size: 104px; letter-spacing: 4px; }
  .brand-name .line-2 { display: block; font-size: 62px; letter-spacing: 3px; }

  .headline {
    position: absolute; left: 50px; top: 252px;
    font-family: "Anton", sans-serif; font-size: 200px; line-height: 1;
    color: var(--navy); transform: scaleX(0.87); transform-origin: left top;
    letter-spacing: -1px;
  }

  .online-list {
    position: absolute; left: 527px; top: 264px;
    list-style: none;
    font-family: "Oswald", sans-serif; font-weight: 700;
    font-size: 46px; line-height: 57px; color: var(--red);
    text-transform: uppercase;
  }

  .feature {
    position: absolute; left: 810px;
    display: flex; align-items: center; gap: 12px;
  }
  .feature.climate { top: 270px; }
  .feature.rates { top: 358px; }
  .feature svg { width: 76px; height: 76px; flex: none; }
  .feature-label {
    font-family: "Oswald", sans-serif; font-weight: 700;
    font-size: 28px; line-height: 31px; color: var(--red);
    text-transform: uppercase;
  }

  .url-band {
    position: absolute; left: 0; top: 458px;
    width: 100%; height: 102px; background: var(--red);
    display: flex; align-items: center; justify-content: center;
  }
  .band-stripes {
    position: absolute; top: 0; width: 52px; height: 100%;
  }
  .band-stripes.left { left: 0; }
  .band-stripes.right { right: 0; }
  .band-stripes span {
    position: absolute; left: 0; width: 100%; height: 3px; background: var(--white);
  }
  .band-stripes span:nth-child(1) { top: 36px; }
  .band-stripes span:nth-child(2) { top: 64px; }
  .url {
    font-family: "Archivo Black", sans-serif; font-size: 44px;
    color: var(--white); text-decoration: none;
    -webkit-text-stroke: 1.5px var(--navy);
    letter-spacing: 0.5px;
  }
</style>
</head>
<body>
<div class="canvas">
  <section class="billboard">
    <div class="brand">
      <div class="brand-dot"></div>
      <div class="brand-name">
        <span class="line-1">Harbor</span>
        <span class="line-2">Self Storage</span>
      </div>
    </div>

    <div class="headline">ONLINE</div>

    <ul class="online-list">
      <li>Rentals</li>
      <li>Payment</li>
      <li>Check Out</li>
    </ul>

    <div class="feature climate">
      <svg viewBox="0 0 80 80" aria-hidden="true" fill="none" stroke="#1a1f6b" stroke-width="4" stroke-linecap="round">
        <path d="M14 30 A28 28 0 0 1 62 18"/>
        <path d="M62 18 l-1 -9 M62 18 l-9 1"/>
        <path d="M66 50 A28 28 0 0 1 18 62"/>
        <path d="M18 62 l1 9 M18 62 l9 -1"/>
        <path d="M35 44 V20 a5 5 0 0 1 10 0 V44"/>
        <circle cx="40" cy="52" r="9"/>
        <path d="M50 22 h5 M50 29 h5 M50 36 h5"/>
      </svg>
      <div class="feature-label">Climate<br>Control</div>
    </div>

    <div class="feature rates">
      <svg viewBox="0 0 80 80" aria-hidden="true" fill="none" stroke="#1a1f6b" stroke-width="4" stroke-linecap="round">
        <circle cx="35" cy="35" r="27"/>
        <path d="M56 56 L72 72" stroke-width="6"/>
        <text x="35" y="47" text-anchor="middle" font-family="Archivo Black, sans-serif" font-size="34" fill="#1a1f6b" stroke="none">$</text>
      </svg>
      <div class="feature-label">Competitive<br>Rates</div>
    </div>

    <div class="url-band">
      <div class="band-stripes left"><span></span><span></span></div>
      <a class="url" href="https://www.harbor-selfstorage-example.com/">www.harbor-selfstorage-example.com</a>
      <div class="band-stripes right"><span></span><span></span></div>
    </div>
  </section>
</div>
</body>
</html>
```